Redesign of Business Card to look more professional and stand out

Business card design. You can lean more about our company by going to dlmfabworks.example. Raised letters would be nice. Company name & Address
DL&M
418 Wrenfield Crest Drive, Suite 140
Birmingham, AL 35999

You can use my name and title: Glenn Marlowe
Business Development Manager

Target Market(s)

Heavy Industrial market, i.e. utilities, chemical plants, paper mills, construction companies

Industry/Entity Type

Construction

Contact Information for Business Card

We provide Project Management & Project Support Services

Font styles to use
Serif

Requirements
Must have
• Company name & Address
• DL&M
• 418 Wrenfield Crest Drive, Suite 140
• Birmingham, AL 35999
Nice to have
• ideas for the back of the card
Should not have
• no crazy colors. needs to look professional and standout.

```html
<!DOCTYPE html>
<html lang="en">
<head>
<meta charset="utf-8">
<title>DL&amp;M Business Card</title>
<link rel="stylesheet" href="https://fonts.googleapis.com/css2?family=Tinos:wght@400;700&display=swap">
<style>
  :root {
    --navy: #1f3666;
    --ink: #141414;
    --paper: #ffffff;
    --rule: #9a9a9a;
    --backdrop: #2c2b2c;
  }
  * { margin: 0; padding: 0; box-sizing: border-box; }
  html, body { width: 1200px; height: 900px; overflow: hidden; background: var(--backdrop); }
  body { position: relative; font-family: "Tinos", "Times New Roman", serif; }

  .card {
    position: absolute;
    width: 600px; height: 343px;
    border-radius: 30px;
    overflow: hidden;
  }
  .card-back { left: 300px; top: 78px; background: var(--navy); }
  .card-front { left: 300px; top: 479px; background: var(--paper); }

  .wordmark { position: absolute; font-weight: 700; letter-spacing: 1px; line-height: 1; white-space: nowrap; }
  .card-back .wordmark { color: var(--paper); font-size: 96px; left: 0; right: 0; top: 122px; text-align: center; }
  .card-front .wordmark { color: var(--navy); font-size: 60px; left: 34px; top: 82px; }

  .divider { position: absolute; left: 240px; top: 95px; }

  .person { position: absolute; left: 300px; top: 100px; }
  .person-name { color: var(--navy); font-size: 26px; font-weight: 400; line-height: 1.1; }
  .person-title { color: var(--ink); font-size: 14px; margin-top: 2px; }

  .contact { position: absolute; font-size: 12.5px; font-weight: 700; color: var(--ink); white-space: nowrap; }
  .contact-row { display: flex; align-items: center; gap: 8px; height: 22px; }
  .contact-phones { left: 270px; top: 176px; }
  .contact-online { left: 384px; top: 176px; }
  .contact-address { left: 270px; top: 226px; }
  .contact-address .contact-row { align-items: flex-start; height: auto; }
  .icon { width: 14px; height: 14px; flex: none; }
  .address-lines { line-height: 1.4; }
</style>
</head>
<body>
  <section class="card card-back" aria-label="Card back">
    <div class="wordmark">DL&amp;M</div>
  </section>

  <section class="card card-front" aria-label="Card front">
    <div class="wordmark">DL&amp;M</div>

    <svg class="divider" width="50" height="150" viewBox="0 0 50 150" aria-hidden="true">
      <line x1="42" y1="2" x2="4" y2="148" stroke="var(--rule)" stroke-width="1.5"/>
    </svg>

    <div class="person">
      <div class="person-name">Glenn Marlowe</div>
      <div class="person-title">Business Development Manager</div>
    </div>

    <div class="contact contact-phones">
      <div class="contact-row">
        <svg class="icon" viewBox="0 0 14 14" aria-hidden="true"><circle cx="7" cy="7" r="6.2" fill="none" stroke="var(--navy)" stroke-width="1"/><path d="M4.6 3.6l1.3 1.6-.7.9c.4 1 1.3 1.9 2.3 2.3l.9-.7 1.6 1.3-.9 1.2C6.6 10 4 7.4 3.5 4.5z" fill="var(--navy)"/></svg>
        <span>205-555-0182</span>
      </div>
      <div class="contact-row">
        <svg class="icon" viewBox="0 0 14 14" aria-hidden="true"><circle cx="7" cy="7" r="7" fill="var(--navy)"/><rect x="4" y="5.5" width="6" height="4" fill="#fff"/><rect x="5" y="3.5" width="4" height="2" fill="#fff"/></svg>
        <span>205-555-0183</span>
      </div>
    </div>

    <div class="contact contact-online">
      <div class="contact-row">
        <svg class="icon" viewBox="0 0 14 14" aria-hidden="true"><circle cx="7" cy="7" r="7" fill="var(--navy)"/><rect x="3.5" y="4.5" width="7" height="5" fill="#fff"/><path d="M3.5 4.5L7 7.5l3.5-3" fill="none" stroke="var(--navy)" stroke-width=".8"/></svg>
        <span>info@dlmfabworks.example</span>
      </div>
      <div class="contact-row">
        <svg class="icon" viewBox="0 0 14 14" aria-hidden="true"><circle cx="7" cy="7" r="6.2" fill="none" stroke="var(--navy)" stroke-width="1"/><circle cx="7" cy="7" r="3.5" fill="none" stroke="var(--navy)" stroke-width=".9"/><line x1="3.5" y1="7" x2="10.5" y2="7" stroke="var(--navy)" stroke-width=".8"/></svg>
        <span>www.dlmfabworks.example</span>
      </div>
    </div>

    <div class="contact contact-address">
      <div class="contact-row">
        <svg class="icon" viewBox="0 0 14 14" aria-hidden="true"><circle cx="7" cy="7" r="6.2" fill="none" stroke="var(--navy)" stroke-width="1"/><path d="M7 3a2.4 2.4 0 0 1 2.4 2.4C9.4 7.2 7 10.5 7 10.5S4.6 7.2 4.6 5.4A2.4 2.4 0 0 1 7 3z" fill="var(--navy)"/><circle cx="7" cy="5.4" r=".9" fill="#fff"/></svg>
        <div class="address-lines">
          <div>DL&amp;M , 418 Wrenfield Crest Drive, Suite 140</div>
          <div>Birmingham, AL 35999</div>
        </div>
      </div>
    </div>
  </section>
</body>
</html>
```